Clean, Throwback Album Art needed

I'm looking for album art for an Indie Rock EP titled "The Quiet Lantern". The artist name is "Martin Kowalczyk"

I'm looking for a design that's wistful and nostalgic, but not depressing. I'm more interested in creative patterns and color combinations than anything else. I've uploaded two examples of album art I really like.

Please no stock images.

In addition to the album art, I will also need two variants of a back cover created in a complementary style- one with a track listing and one with marketing copy (e.g. Free download available at ___ ). These back covers do not have to be incredibly detailed, but can't just be text overlaid on top of of the front cover.

Details for back cover (track names, credits, etc.) will be provided to whoever submits the winning front cover design.

Requirements
Should not have
• No stock images. I need to know that I fully own the copyright to whatever work is produced.

```html
<!DOCTYPE html>
<html lang="en">
<head>
<meta charset="utf-8">
<title>The Quiet Lantern – Martin Kowalczyk</title>
<link rel="stylesheet" href="https://fonts.googleapis.com/css2?family=Anton&family=Archivo+Black&family=Archivo:wght@500;700&display=swap">
<style>
  :root {
    --page: #ffffff;
    --paper: #efe9e3;
    --paper-warm: #e6d6cc;
    --ink: #1d1a18;
    --spine: #000000;
    --spine-text: #ffffff;
    --magenta: rgba(184, 58, 122, 0.95);
    --red: rgba(184, 48, 42, 0.95);
    --ochre: rgba(140, 106, 44, 0.95);
    --violet: rgba(122, 60, 154, 0.95);
    --green: rgba(79, 143, 53, 0.95);
    --mist: #cfd6d3;
    --blue: rgba(74, 85, 200, 0.9);
    --lime: rgba(183, 227, 106, 0.85);
    --veil: rgba(255, 255, 255, 0.55);
  }
  * { margin: 0; padding: 0; box-sizing: border-box; }
  html, body { width: 1200px; height: 1200px; overflow: hidden; background: var(--page); }
  body { position: relative; font-family: "Archivo", Arial, sans-serif; color: var(--ink); }

  /* Front cover */
  .front-cover {
    position: absolute; left: 314px; top: 42px; width: 575px; height: 575px;
    background:
      radial-gradient(circle 160px at 20% 85%, rgba(214,150,120,0.35), transparent),
      radial-gradient(circle 140px at 88% 40%, rgba(170,120,200,0.4), transparent),
      radial-gradient(circle 110px at 65% 15%, rgba(230,210,120,0.35), transparent),
      linear-gradient(160deg, var(--paper), var(--paper-warm));
    box-shadow: 1px 1px 3px rgba(0,0,0,0.45);
    overflow: hidden;
  }
  .front-artwork {
    position: absolute; inset: 0;
    background:
      radial-gradient(circle 95px at 282px 206px, var(--ochre), transparent),
      radial-gradient(circle 85px at 326px 290px, var(--red), transparent),
      radial-gradient(circle 100px at 440px 250px, var(--violet), transparent),
      radial-gradient(circle 100px at 206px 380px, var(--magenta), transparent),
      radial-gradient(circle 100px at 372px 396px, var(--green), transparent);
  }
  .front-title {
    position: absolute; left: 0; top: 0; width: 100%; height: 100%;
    font-family: "Anton", Impact, sans-serif; font-weight: 400; font-size: 44px;
    line-height: 44px; letter-spacing: 1px; text-transform: uppercase; color: var(--ink);
  }
  .title-line {
    position: absolute; display: block; white-space: nowrap;
    transform: rotate(-35deg); transform-origin: left bottom;
  }
  .title-line--first { left: 30px; top: 150px; }
  .title-line--second { left: 100px; top: 182px; }
  .front-artist { position: absolute; left: 0; top: 0; width: 575px; height: 575px; }
  .front-artist text {
    font-family: "Archivo Black", Arial, sans-serif; font-size: 42px; fill: var(--ink);
    word-spacing: 40px;
  }

  /* Back cover */
  .back-cover {
    position: absolute; left: 275px; top: 649px; width: 653px; height: 511px;
    display: flex; box-shadow: 1px 1px 3px rgba(0,0,0,0.4);
  }
  .spine {
    position: relative; width: 27px; height: 100%; background: var(--spine);
    color: var(--spine-text); font-family: "Archivo", Arial, sans-serif;
    font-weight: 700; font-size: 12.5px; letter-spacing: 0.3px; white-space: nowrap;
  }
  .spine-text { position: absolute; left: 50%; }
  .spine--left .spine-text { transform: translateX(-50%) rotate(180deg); writing-mode: vertical-rl; }
  .spine--left .spine-text--top { top: 12px; }
  .spine--left .spine-text--bottom { bottom: 28px; }
  .spine--right .spine-text { transform: translateX(-50%); writing-mode: vertical-rl; }
  .spine--right .spine-text--top { top: 12px; }
  .spine--right .spine-text--bottom { bottom: 28px; }

  .back-panel {
    position: relative; flex: 1; height: 100%; overflow: hidden;
    background:
      radial-gradient(circle 110px at 90px 60px, rgba(100,190,70,0.7), transparent),
      radial-gradient(circle 150px at 590px 110px, var(--blue), transparent),
      radial-gradient(circle 120px at 570px 290px, var(--lime), transparent),
      radial-gradient(circle 120px at 150px 470px, rgba(150,60,190,0.8), transparent),
      radial-gradient(circle 130px at 410px 460px, rgba(80,140,50,0.85), transparent),
      radial-gradient(circle 90px at 330px 40px, rgba(220,150,110,0.5), transparent),
      linear-gradient(180deg, var(--mist), #d9ddda);
  }
  .back-title {
    position: absolute; left: 0; right: 0; top: 38px; text-align: center;
    font-weight: 500; font-size: 18px; letter-spacing: 0.2px; color: var(--ink);
  }
  .track-box {
    position: absolute; left: 32px; top: 110px; width: 530px; height: 288px;
    background: var(--veil);
  }
  .track-list {
    position: absolute; list-style: none; font-weight: 500; font-size: 12.5px;
    line-height: 27.6px; letter-spacing: 0.1px; color: var(--ink);
  }
  .track-list--a { left: 52px; top: 50px; }
  .track-list--b { left: 324px; top: 52px; }
</style>
</head>
<body>
  <section class="front-cover" aria-label="Front cover">
    <div class="front-artwork" role="img" aria-label="Watercolour illustration of stacked isometric cubes in ochre, red, violet, magenta and green with paint splatters"></div>
    <h1 class="front-title">
      <span class="title-line title-line--first">The Quiet</span>
      <span class="title-line title-line--second">Lantern</span>
    </h1>
    <svg class="front-artist" viewBox="0 0 575 575" aria-label="Martin Kowalczyk">
      <defs><path id="artist-arc" d="M 110 440 Q 330 640 540 420"/></defs>
      <text><textPath href="#artist-arc" startOffset="50%" text-anchor="middle">Martin Kowalczyk</textPath></text>
    </svg>
  </section>

  <section class="back-cover" aria-label="Back cover">
    <div class="spine spine--left">
      <span class="spine-text spine-text--top">THE QUIET LANTERN</span>
      <span class="spine-text spine-text--bottom">MARTIN KOWALCZYK</span>
    </div>
    <div class="back-panel" role="img" aria-label="Faded watercolour cube pattern in green, violet, blue and lime">
      <h2 class="back-title">THE QUIET LANTERN</h2>
      <div class="track-box">
        <ol class="track-list track-list--a">
          <li>SONG TITLE SONG TITLE</li>
          <li>SONG TITLE SONG TITLE</li>
          <li>SONG TITLE SONG TITLE</li>
          <li>SONG TITLE SONG TITLE</li>
          <li>SONG TITLE SONG TITLE</li>
          <li>SONG TITLE SONG TITLE</li>
          <li>SONG TITLE SONG TITLE</li>
        </ol>
        <ol class="track-list track-list--b">
          <li>SONG TITLE SONG TITLE</li>
          <li>SONG TITLE SONG TITLE</li>
          <li>SONG TITLE SONG TITLE</li>
          <li>SONG TITLE SONG TITLE</li>
          <li>SONG TITLE SONG TITLE</li>
          <li>SONG TITLE SONG TITLE</li>
          <li>SONG TITLE SONG TITLE</li>
        </ol>
      </div>
    </div>
    <div class="spine spine--right">
      <span class="spine-text spine-text--top">MARTIN KOWALCZYK</span>
      <span class="spine-text spine-text--bottom">THE QUIET LANTERN</span>
    </div>
  </section>
</body>
</html>
```